Hi Tobias, I need some designs for the front door and windows of our clinic, and some internal walls.

I have attached a picture of the front door and windows.
On them it needs
Sports Medicine
Pain Medicine
9371 6200
www.corvelhealthhub.com.au
Maybe the logo.

I will get it printed as stickers. Can you keep the blues, the font, and the Hexagon thing going.

I have also included 2 walls that I am thinking I would put a graphic on. One is behind the desk directly facing the front door/windows, the other is off to the right.

For the wall facing the door, maybe we have the Logo on it

For the other wall, maybe we put "Pain is a thief. Take back what's yours" in the cursive you have done before

See what you can magic up for me.

Cheers

Rob

```html
<!DOCTYPE html>
<html lang="en">
<head>
<meta charset="utf-8">
<title>Halvary Motion Clinic – Window and Wall Graphics</title>
<link rel="stylesheet" href="https://fonts.googleapis.com/css2?family=Barlow+Condensed:wght@600;700&family=Playfair+Display:ital,wght@1,700&display=swap">
<style>
  :root {
    --blue-deep: #1553ae;
    --blue-bright: #29b0e8;
    --blue-mid: #1f63c4;
    --white: #ffffff;
    --canvas: #eef0f3;
    --sky: #5a9fdc;
    --grass: #6ea84a;
    --track: #9c8870;
    --skin: #b57a52;
  }
  * { margin: 0; padding: 0; box-sizing: border-box; }
  html, body { width: 1200px; height: 1117px; overflow: hidden; background: var(--canvas); }
  .canvas { position: relative; width: 1200px; height: 1117px; font-family: "Barlow Condensed", "Arial Narrow", sans-serif; }

  .piece { position: absolute; }
  .piece > svg { position: absolute; inset: 0; width: 100%; height: 100%; display: block; }

  .window-banner { width: 330px; height: 111px; }
  .window-banner .label {
    position: absolute; inset: 0; display: flex; align-items: center; justify-content: center;
    color: var(--white); font-weight: 700; letter-spacing: -0.5px; padding-bottom: 6px;
  }
  .banner-sports { left: 91px; top: 203px; }
  .banner-pain { left: 94px; top: 324px; }
  .banner-phone { left: 800px; top: 202px; }
  .banner-web { left: 798px; top: 325px; }
  .banner-sports .label, .banner-pain .label { font-size: 42px; }
  .banner-phone .label { font-size: 54px; }
  .banner-web .label { font-size: 24px; }

  .door-panel { width: 150px; height: 276px; }
  .door-left { left: 445px; top: 202px; }
  .door-right { left: 628px; top: 204px; }
  .door-panel .contact-pill {
    position: absolute; left: 12px; top: 48px; width: 114px; height: 21px;
    border: 2px solid var(--blue-deep); border-radius: 3px;
    display: flex; align-items: center; gap: 4px; padding-left: 2px;
    color: var(--blue-deep); font-weight: 700; white-space: nowrap; overflow: hidden;
  }
  .contact-pill .pill-icon { width: 20px; height: 20px; flex: none; margin-left: -6px; }
  .door-left .contact-pill { font-size: 15px; }
  .door-right .contact-pill { font-size: 8.5px; }
  .door-panel .brand-name {
    position: absolute; left: 14px; top: 80px; width: 100px;
    color: var(--blue-deep); font-weight: 700; font-size: 28px; line-height: 0.95;
  }

  .wall-quote { left: 140px; top: 655px; width: 459px; height: 256px; }
  .wall-quote .quote-lead {
    position: absolute; left: 0; right: 0; top: 14px; text-align: center;
    font-family: "Playfair Display", Georgia, serif; font-style: italic; font-weight: 700;
    font-size: 56px; color: var(--blue-deep); letter-spacing: -0.5px;
  }
  .wall-quote .quote-answer {
    position: absolute; left: 40px; right: 0; top: 106px; text-align: center;
    color: var(--white); font-weight: 700; font-size: 64px; line-height: 0.92; letter-spacing: -0.5px;
  }

  .wall-brand { left: 696px; top: 739px; width: 459px; height: 249px; }
  .wall-brand .brand-name {
    position: absolute; left: 148px; top: 22px; width: 180px; text-align: left;
    color: var(--blue-deep); font-weight: 700; font-size: 52px; line-height: 0.95;
  }
  .wall-brand .brand-url {
    position: absolute; left: 30px; right: 0; bottom: 8px; height: 34px;
    display: flex; align-items: center; justify-content: center;
    color: var(--white); font-weight: 700; font-size: 24px;
  }
</style>
</head>
<body>
<main class="canvas">

  <section class="piece window-banner banner-sports">
    <svg viewBox="0 0 330 111" preserveAspectRatio="none" aria-hidden="true">
      <rect width="330" height="111" fill="var(--white)"/>
      <polygon points="0,0 330,0 330,4 14,20 0,30" fill="var(--blue-bright)"/>
      <polygon points="14,20 330,4 316,92 3,111" fill="var(--blue-deep)"/>
    </svg>
    <p class="label">Sports Medicine</p>
  </section>

  <section class="piece window-banner banner-pain">
    <svg viewBox="0 0 330 111" preserveAspectRatio="none" aria-hidden="true">
      <rect width="330" height="111" fill="var(--white)"/>
      <polygon points="0,0 330,0 330,4 14,20 0,30" fill="var(--blue-bright)"/>
      <polygon points="14,20 330,4 316,92 3,111" fill="var(--blue-deep)"/>
    </svg>
    <p class="label">Pain Medicine</p>
  </section>

  <section class="piece window-banner banner-phone">
    <svg viewBox="0 0 330 111" preserveAspectRatio="none" aria-hidden="true">
      <rect width="330" height="111" fill="var(--white)"/>
      <polygon points="0,0 330,0 330,4 14,20 0,30" fill="var(--blue-bright)"/>
      <polygon points="14,20 330,4 316,92 3,111" fill="var(--blue-deep)"/>
    </svg>
    <p class="label">9371 6200</p>
  </section>

  <section class="piece window-banner banner-web">
    <svg viewBox="0 0 330 111" preserveAspectRatio="none" aria-hidden="true">
      <rect width="330" height="111" fill="var(--white)"/>
      <polygon points="0,0 330,0 330,4 14,20 0,30" fill="var(--blue-bright)"/>
      <polygon points="14,20 330,4 316,92 3,111" fill="var(--blue-deep)"/>
    </svg>
    <p class="label">corvelhealthhub.com.au</p>
  </section>

  <section class="piece door-panel door-left">
    <svg viewBox="0 0 150 276" preserveAspectRatio="none" aria-hidden="true">
      <polygon points="0,0 142,0 112,250 0,250" fill="var(--white)"/>
      <polygon points="150,5 150,276 60,245 120,230" fill="var(--blue-mid)"/>
    </svg>
    <div class="contact-pill">
      <svg class="pill-icon" viewBox="0 0 20 20" aria-hidden="true">
        <circle cx="10" cy="10" r="10" fill="var(--blue-deep)"/>
        <path d="M6.5 5.5l2 -0.5 1 2.5 -1.2 1c0.6 1.3 1.6 2.3 2.9 2.9l1 -1.2 2.5 1 -0.5 2c-4.5 0 -8 -3.5 -7.7 -7.7z" fill="var(--white)"/>
      </svg>
      <span>9371 6200</span>
    </div>
    <p class="brand-name">HALVARY MOTION CLINIC</p>
  </section>

  <section class="piece door-panel door-right">
    <svg viewBox="0 0 150 276" preserveAspectRatio="none" aria-hidden="true">
      <polygon points="0,0 142,0 112,250 0,250" fill="var(--white)"/>
      <polygon points="150,5 150,276 60,245 120,230" fill="var(--blue-mid)"/>
    </svg>
    <div class="contact-pill">
      <svg class="pill-icon" viewBox="0 0 20 20" aria-hidden="true">
        <circle cx="10" cy="10" r="10" fill="var(--blue-deep)"/>
        <circle cx="10" cy="10" r="5.5" fill="none" stroke="var(--white)" stroke-width="1.2"/>
        <path d="M4.5 10h11M10 4.5v11" stroke="var(--white)" stroke-width="1.2"/>
      </svg>
      <span>corvelhealthhub.com.au</span>
    </div>
    <p class="brand-name">HALVARY MOTION CLINIC</p>
  </section>

  <section class="piece wall-quote">
    <svg viewBox="0 0 459 256" preserveAspectRatio="none" aria-hidden="true">
      <rect width="459" height="256" fill="var(--white)"/>
      <polygon points="45,88 459,97 459,256 0,256" fill="var(--blue-deep)"/>
    </svg>
    <p class="quote-lead">Pain is a thief</p>
    <p class="quote-answer">Take back<br>what’s yours</p>
  </section>

  <section class="piece wall-brand">
    <svg viewBox="0 0 459 249" preserveAspectRatio="none" aria-hidden="true">
      <rect width="459" height="249" fill="var(--white)"/>
    </svg>
    <svg viewBox="0 0 459 249" preserveAspectRatio="none" role="img" aria-label="Photo of a golfer mid-swing on a green course under a blue sky">
      <defs>
        <linearGradient id="golf-tones" x1="0" y1="0" x2="0" y2="1">
          <stop offset="0" stop-color="var(--sky)"/>
          <stop offset="0.55" stop-color="#8fc1ea"/>
          <stop offset="1" stop-color="var(--grass)"/>
        </linearGradient>
      </defs>
      <polygon points="0,0 142,0 112,220 0,220" fill="url(#golf-tones)"/>
    </svg>
    <svg viewBox="0 0 459 249" preserveAspectRatio="none" role="img" aria-label="Photo of a runner tying a red running shoe on a gravel track">
      <defs>
        <linearGradient id="runner-tones" x1="0" y1="0" x2="1" y2="1">
          <stop offset="0" stop-color="var(--skin)"/>
          <stop offset="0.5" stop-color="#6f5a48"/>
          <stop offset="1" stop-color="var(--track)"/>
        </linearGradient>
      </defs>
      <polygon points="350,0 459,0 459,200 326,200" fill="url(#runner-tones)"/>
    </svg>
    <svg viewBox="0 0 459 249" preserveAspectRatio="none" aria-hidden="true">
      <polygon points="12,200 459,200 459,249 0,249" fill="var(--blue-deep)"/>
    </svg>
    <p class="brand-name">HALVARY MOTION CLINIC</p>
    <p class="brand-url">corvelhealthhub.com.au</p>
  </section>

</main>
</body>
</html>
```